Marlowe Restoration & Remodeling Group LLC

Roofing, windows, gutters services offered.
0% 6 months interest free financing
Vernon windows
Whitfield windows
KTR roofing shingles
ULP roofing shingles
Offering 30-50 year warranties.
Accepting all major credit cards, checks
Emergency services available

Target Market(s)

Roofing contractors

Industry/Entity Type

Roofing

Number of Pages Required

3 page

Font styles to use
Sans Serif

Requirements
Must have
• MUST HAVE SEO all necessary codes!!!!!!!!!!
• also I want button for "schedule appointment" so I can receive notification of an appointment, and also need live calendar integrated in that button
Nice to have
• Modern, professional site

```html
<!DOCTYPE html>
<html lang="en">
<head>
<meta charset="utf-8">
<title>Marlowe Restoration &amp; Remodeling Group LLC | Roofing, Windows &amp; Gutters</title>
<meta name="description" content="Marlowe Restoration & Remodeling Group LLC offers roofing, windows and gutters with 30-50 year warranties, emergency services and 0% 6 months interest free financing.">
<meta name="viewport" content="width=1200">
<link href="https://fonts.googleapis.com/css2?family=Cinzel:wght@400;500&family=Lato:wght@400;700&display=swap" rel="stylesheet">
<style>
:root{
  --green:#4c9a36;
  --green-dark:#3a8a2b;
  --green-text:#3a9a3c;
  --blue:#1f72b8;
  --blue-mid:#1a5d9f;
  --blue-dark:#0f3b70;
  --ink:#555b61;
  --line:#d9dde1;
  --white:#ffffff;
  --star:#f2c22f;
}
*{box-sizing:border-box;margin:0;padding:0}
html,body{width:1200px;height:4281px;overflow:hidden}
body{font-family:'Lato',sans-serif;color:var(--ink);background:var(--white);position:relative}
.abs{position:absolute}
.serif{font-family:'Cinzel',serif}

/* header */
.site-header{position:absolute;top:0;left:0;width:1200px;height:115px;background:var(--white)}
.brand{position:absolute;left:78px;top:30px;display:flex;align-items:center;gap:10px}
.brand-mark{width:34px;height:34px;border-radius:50%;background:var(--green)}
.brand-name{font-family:'Lato',sans-serif;font-size:13px;line-height:16px;color:var(--blue);font-weight:700;width:170px}
.contact-pill{position:absolute;top:32px;display:flex;align-items:center;gap:16px;white-space:nowrap}
.contact-pill .ring{width:48px;height:48px;border-radius:50%;border:2px solid var(--green);display:flex;align-items:center;justify-content:center;flex:none}
.contact-pill small{display:block;font-size:13px;color:#6c7278;letter-spacing:.3px}
.contact-pill strong{display:block;font-weight:400;font-size:19px;color:#5d636a;margin-top:2px}

.main-nav{position:absolute;top:115px;left:0;width:1200px;height:51px;background:linear-gradient(#2273b9,#1a5c9d)}
.main-nav ul{list-style:none;position:absolute;left:77px;top:0;display:flex;height:51px}
.main-nav li{color:var(--white);font-size:14px;line-height:51px;padding:0 18px;letter-spacing:.3px}
.main-nav li.active{background:var(--green);padding:0 25px}
.btn-schedule{position:absolute;right:78px;top:0;height:51px;width:249px;background:var(--green);color:var(--white);font-family:'Cinzel',serif;font-size:16px;line-height:51px;text-align:center;letter-spacing:.5px}

/* hero */
.hero{position:absolute;top:166px;left:0;width:1200px;height:552px;background:linear-gradient(180deg,#3b4452 0%,#2a2d31 45%,#263020 80%,#33452a 100%)}
.hero h1{position:absolute;top:200px;width:100%;text-align:center;font-family:'Cinzel',serif;font-weight:400;font-size:50px;color:var(--white)}
.hero p{position:absolute;top:282px;width:100%;text-align:center;font-size:30px;color:var(--white)}
.hero-tab{position:absolute;top:686px;left:354px;width:490px;height:65px}
.hero-tab span{position:absolute;top:23px;color:var(--white);font-size:14px;display:flex;align-items:center;gap:10px;white-space:nowrap}

/* welcome */
.welcome h2{position:absolute;left:80px;top:822px;font-family:'Cinzel',serif;font-weight:400;font-size:40px;line-height:49px;color:var(--green-text)}
.welcome h2 .blue{color:var(--blue)}
.text-sm{font-size:13.5px;line-height:25px;color:#6a7076}
.welcome-logo{position:absolute;left:78px;top:1056px;width:186px;height:178px;display:flex;align-items:center;justify-content:center}
.welcome-logo .disc{width:150px;height:150px;border-radius:50%;background:linear-gradient(135deg,#2a80c4,#3f9a3a);display:flex;align-items:center;justify-content:center;color:var(--white);font-size:18px;font-weight:700}
.btn-blue{position:absolute;background:linear-gradient(#1f6db0,#0f3f78);color:var(--white);font-family:'Cinzel',serif;text-align:center}

.quote{position:absolute;left:768px;top:834px;width:356px;height:397px;border:1px solid var(--line);border-radius:4px;background:var(--white)}
.quote-head{position:absolute;left:-1px;top:-1px;width:356px;height:84px}
.quote-head h3{position:absolute;top:22px;width:100%;text-align:center;font-family:'Cinzel',serif;font-weight:400;font-size:24px;color:var(--white);letter-spacing:.5px}
.field{position:absolute;left:28px;width:303px;border:1px solid #cfd4d8;background:#f7f8f9;font-size:13px;color:#777;padding:10px 16px}

/* services */
.service{position:absolute;left:0;width:1200px;overflow:hidden}
.service.dark{background:linear-gradient(180deg,#2b7ec4 0%,#1d5e9f 55%,#153f7a 100%)}
.service.light{background:linear-gradient(180deg,#dfe4ea 0%,#cfd8e0 100%)}
.services-title{position:absolute;top:1365px;width:100%;text-align:center;font-family:'Cinzel',serif;font-weight:400;font-size:40px;color:var(--white)}
.icon-circle{position:absolute;width:230px;height:230px;border-radius:50%;background:var(--green);border:9px solid var(--white);display:flex;align-items:center;justify-content:center}
.service h3{position:absolute;font-family:'Cinzel',serif;font-weight:400;font-size:32px;letter-spacing:.5px}
.service p{position:absolute;width:560px;font-size:13.5px;line-height:25px}
.dark h3,.dark p{color:var(--white)}
.light h3{color:var(--blue)}
.light p{color:#4e5459}

/* financing */
.financing h2{position:absolute;top:2606px;width:100%;text-align:center;font-family:'Cinzel',serif;font-weight:400;font-size:40px;color:var(--blue)}
.financing h2 .g{color:var(--green-text)}
.product{position:absolute;top:2689px;width:219px;height:220px;border:1px solid var(--line);text-align:center}
.product svg{position:absolute;left:73px;top:52px}
.product span{position:absolute;top:157px;left:0;width:100%;font-size:16px;color:#4e5459}

/* testimonials */
.testimonials{position:absolute;top:3000px;left:0;width:1200px;height:593px;background:linear-gradient(180deg,#2478bd 0%,#1a5a9b 55%,#123f78 100%)}
.testimonials h2{position:absolute;top:56px;width:100%;text-align:center;font-family:'Cinzel',serif;font-weight:400;font-size:40px;color:var(--white)}
.t-card{position:absolute;top:133px;width:323px;background:rgba(255,255,255,.1);padding:28px 16px 0 16px}
.t-card p{font-size:13.5px;line-height:25px;color:var(--white)}
.t-card .who{margin-top:16px;display:flex;justify-content:space-between;align-items:center;color:var(--white);font-size:13.5px;padding-right:20px}
.stars{color:var(--star);font-size:22px;letter-spacing:1px}

/* newsletter */
.newsletter h2{position:absolute;top:3648px;width:100%;text-align:center;font-family:'Cinzel',serif;font-weight:400;font-size:40px;color:var(--green-text)}
.newsletter p{position:absolute;top:3719px;width:100%;text-align:center}
.subscribe{position:absolute;left:278px;top:3801px;width:643px;height:62px;border:1px solid #cfd4d8;border-radius:31px;background:var(--white)}
.subscribe span{position:absolute;left:36px;top:21px;font-size:13.5px;color:#666}
.subscribe .btn-blue{right:-1px;top:-1px;width:190px;height:62px;border-radius:31px;line-height:62px;font-size:20px;letter-spacing:1px}

/* footer */
.site-footer{position:absolute;top:3947px;left:0;width:1200px;height:271px;background:linear-gradient(180deg,#2274ba 0%,#154a88 100%);color:var(--white)}
.footer-brand{position:absolute;left:78px;top:94px;display:flex;align-items:center;gap:14px}
.footer-brand .sq{width:40px;height:40px;border-radius:50%;background:var(--white)}
.footer-brand span{font-size:18px;line-height:24px;width:230px}
.site-footer h4{position:absolute;top:62px;font-family:'Cinzel',serif;font-weight:400;font-size:22px;letter-spacing:.5px}
.site-footer ul{position:absolute;list-style:none;font-size:13.5px}
.site-footer ul li{margin-bottom:20px;display:flex;align-items:center;gap:12px}
.site-footer ul li:before{content:"";width:9px;height:9px;border-radius:50%;background:var(--white)}
.contact-line{position:absolute;left:801px;font-size:13.5px;line-height:25px;display:flex;gap:14px}
.copyright{position:absolute;top:4218px;left:0;width:1200px;height:63px;background:var(--green);color:var(--white);text-align:center;line-height:63px;font-size:13.5px}
</style>
</head>
<body>

<header class="site-header">
  <div class="brand"><div class="brand-mark"></div><div class="brand-name">Marlowe Restoration &amp; Remodeling Group LLC</div></div>
  <div class="contact-pill" style="left:596px">
    <div class="ring"><svg width="20" height="16" viewBox="0 0 20 16"><rect x="1" y="2" width="18" height="13" rx="1" fill="var(--blue)"/><path d="M1 3l9 7 9-7" fill="none" stroke="#fff" stroke-width="1.6"/></svg></div>
    <div><small>EMAIL US ON</small><strong>info@marloweremodel.com</strong></div>
  </div>
  <div class="contact-pill" style="left:928px">
    <div class="ring"><svg width="20" height="20" viewBox="0 0 24 24"><path d="M6.6 10.8a15 15 0 006.6 6.6l2.2-2.2a1 1 0 011-.25 11.4 11.4 0 003.6.6 1 1 0 011 1V20a1 1 0 01-1 1A17 17 0 013 4a1 1 0 011-1h3.5a1 1 0 011 1c0 1.25.2 2.45.6 3.6a1 1 0 01-.25 1z" fill="var(--blue)"/></svg></div>
    <div><small>CALL US ON</small><strong>555 014 7290</strong></div>
  </div>
</header>

<nav class="main-nav">
  <ul><li class="active">HOME</li><li>ABOUT US</li><li>SERVICES</li><li>TESTIMONIALS</li><li>CONTACT</li></ul>
  <a class="btn-schedule">SCHEDULE APPOINTMENT</a>
</nav>

<section class="hero" role="img" aria-label="Dusk photograph of a large Tudor-style home with a lawn in front">
  <h1>30-50 YEAR WARRANTIES.</h1>
  <p>Emergency services available</p>
</section>
<div class="hero-tab">
  <svg width="490" height="65" viewBox="0 0 490 65" class="abs" style="left:0;top:0">
    <defs><linearGradient id="tabBlue" x1="0" x2="0" y1="0" y2="1"><stop offset="0" stop-color="#1f6db0"/><stop offset="1" stop-color="#0f3f78"/></linearGradient></defs>
    <polygon points="20,0 241,0 241,65 20,65 0,32" fill="var(--green)"/>
    <polygon points="241,0 470,0 490,32 470,65 241,65" fill="url(#tabBlue)"/>
    <polyline points="26,2 8,32 26,63" fill="none" stroke="#fff" stroke-width="3"/>
    <polyline points="464,2 482,32 464,63" fill="none" stroke="#fff" stroke-width="3"/>
  </svg>
  <span style="left:56px"><svg width="17" height="17" viewBox="0 0 24 24"><path d="M6.6 10.8a15 15 0 006.6 6.6l2.2-2.2a1 1 0 011-.25 11.4 11.4 0 003.6.6 1 1 0 011 1V20a1 1 0 01-1 1A17 17 0 013 4a1 1 0 011-1h3.5a1 1 0 011 1c0 1.25.2 2.45.6 3.6a1 1 0 01-.25 1z" fill="#fff"/></svg>555 014 7290</span>
  <span style="left:262px"><svg width="18" height="14" viewBox="0 0 20 16"><rect x="1" y="2" width="18" height="13" rx="1" fill="#fff"/><path d="M1 3l9 7 9-7" fill="none" stroke="#1a5d9f" stroke-width="1.6"/></svg>info@marloweremodel.com</span>
</div>

<section class="welcome">
  <h2>WELCOME TO MARLOWE<br><span class="blue">RESTORATION REMODELING</span></h2>
  <p class="text-sm abs" style="left:80px;top:944px;width:610px">Lorem Ipsum is simply dummy text of the printing and typesetting industry. Lorem Ipsum has been the industry's standard dummy text ever since the 1500s, when an unknown printer took a galley of type and scrambled it to make a type specimen book.</p>
  <div class="welcome-logo"><div class="disc">Marlowe</div></div>
  <p class="text-sm abs" style="left:329px;top:1047px;width:360px">It has survived not only five centuries, but also the leap into electronic typesetting, remaining essentially unchanged. It was popularised in the 1960s with the release of Letraset sheets containing Lorem Ipsum passages, and more recently with desktop publishing.</p>
  <a class="btn-blue" style="left:326px;top:1192px;width:188px;height:46px;line-height:46px;font-size:17px">READ MORE</a>

  <form class="quote">
    <svg class="quote-head" width="356" height="84" viewBox="0 0 356 84"><polygon points="0,0 356,0 356,58 178,84 0,58" fill="url(#tabBlue)"/></svg>
    <div class="quote-head"><h3>GET FREE QUOTE</h3></div>
    <div class="field" style="top:112px;height:40px">Name</div>
    <div class="field" style="top:163px;height:42px">Email</div>
    <div class="field" style="top:216px;height:93px">Message</div>
    <a class="btn-blue" style="left:28px;top:319px;width:303px;height:42px;line-height:42px;font-size:20px;letter-spacing:1px">SEND</a>
  </form>
</section>

<h2 class="services-title" style="z-index:2">OUR SERVICES</h2>
<section class="service dark" style="top:1323px;height:437px" aria-label="Roofing">
  <div class="icon-circle" style="left:141px;top:128px">
    <svg width="118" height="88" viewBox="0 0 118 88"><polygon points="59,4 2,54 12,62 59,21 106,62 116,54 96,36 96,10 84,10 84,26" fill="#fff"/><polygon points="20,58 59,25 98,58 98,88 20,88" fill="#fff"/><g fill="var(--green)"><rect x="46" y="56" width="11" height="9"/><rect x="61" y="56" width="11" height="9"/><rect x="46" y="68" width="11" height="9"/><rect x="61" y="68" width="11" height="9"/></g></svg>
  </div>
  <h3 style="left:485px;top:160px">ROOFING</h3>
  <p style="left:485px;top:215px">Lorem Ipsum is simply dummy text of the printing and typesetting industry. Lorem Ipsum has been the industry's standard dummy text ever since the 1500s, when an unknown printer took a galley of type and scrambled it to make a type specimen book It has survived not only five centuries, but also the leap into electronic typesetting.</p>
</section>
<section class="service light" style="top:1760px;height:396px" aria-label="Windows">
  <div class="icon-circle" style="left:809px;top:83px">
    <svg width="104" height="104" viewBox="0 0 104 104" fill="#fff"><rect x="0" y="0" width="48" height="48"/><rect x="56" y="0" width="48" height="48"/><rect x="0" y="56" width="48" height="48"/><rect x="56" y="56" width="48" height="48"/></svg>
  </div>
  <h3 style="left:136px;top:120px">WINDOWS</h3>
  <p style="left:136px;top:175px">Lorem Ipsum is simply dummy text of the printing and typesetting industry. Lorem Ipsum has been the industry's standard dummy text ever since the 1500s, when an unknown printer took a galley of type and scrambled it to make a type specimen book It has survived not only five centuries, but also the leap into electronic typesetting.</p>
</section>
<section class="service dark" style="top:2156px;height:395px" aria-label="Gutters">
  <div class="icon-circle" style="left:141px;top:86px">
    <svg width="116" height="96" viewBox="0 0 116 96" fill="#fff"><path d="M0 2h116v18c-8 10-26 14-42 14H56v14h16v-8h14v14c0 10-8 14-14 14h-16v28H38V56c0-8 6-12 14-12h6V34H18C8 34 0 26 0 16z"/></svg>
  </div>
  <h3 style="left:485px;top:120px">GUTTERS</h3>
  <p style="left:485px;top:175px">Lorem Ipsum is simply dummy text of the printing and typesetting industry. Lorem Ipsum has been the industry's standard dummy text ever since the 1500s, when an unknown printer took a galley of type and scrambled it to make a type specimen book It has survived not only five centuries, but also the leap into electronic typesetting.</p>
</section>

<section class="financing">
  <h2><span class="g">0% 6 MONTHS</span> INTEREST FREE <span class="g">FINANCING</span></h2>
  <div class="product" style="left:116px"><svg width="74" height="66" viewBox="0 0 74 66" fill="none" stroke="var(--green)" stroke-width="2.5"><rect x="2" y="2" width="70" height="62"/><rect x="10" y="8" width="54" height="50"/><path d="M16 16h42M16 24h42M16 32h42M16 40h42M16 48h42"/></svg><span>Vernon windows</span></div>
  <div class="product" style="left:367px"><svg width="66" height="70" viewBox="0 0 66 70" fill="none" stroke="var(--green)" stroke-width="2.5"><rect x="2" y="2" width="62" height="66"/><rect x="10" y="10" width="46" height="58"/><path d="M33 10v58M10 40h46M18 24l6-8M40 24l6-8"/></svg><span>Whitfield windows</span></div>
  <div class="product" style="left:617px"><svg width="82" height="62" viewBox="0 0 82 62" fill="none" stroke="var(--green)" stroke-width="2.5"><polygon points="2,4 56,4 80,58 26,58"/><path d="M20 4l24 54M38 4l24 54M8 18h54M14 31h54M20 44h54"/></svg><span>KTR roofing shingles</span></div>
  <div class="product" style="left:866px"><svg width="80" height="66" viewBox="0 0 80 66" fill="none" stroke="var(--green)" stroke-width="2.5"><path d="M2 64V14Q40-4 78 14v50M2 64h76M16 64V8M30 64V4M50 64V4M64 64V8M2 28h76M2 44h76"/></svg><span>ULP roofing shingles</span></div>
</section>

<section class="testimonials">
  <h2>CLIENT TESTIMONIALS</h2>
  <article class="t-card" style="left:76px;height:322px"><p>Lorem Ipsum is simply dummy text of the printing and typesetting industry. Lorem Ipsum has been the industry's standard dummy text ever since the 1500s, when an unknown printer took a galley of type and scrambled it to make a type specimen book. It has survived not only five centuries, but also the leap into electronic typesetting.</p><div class="who"><span>- NAME SURNAME</span><span class="stars">★★★★★</span></div></article>
  <article class="t-card" style="left:439px;height:362px"><p>Lorem Ipsum is simply dummy text of the printing and typesetting industry. Lorem Ipsum has been the industry's standard dum text ever since the 1500s, when an unknown printer took a galley of type and scrambled it to make a type specimen book. It has survived not only five centuries, but also the leap into electronic typesetting, remaining essentially unchanged.</p><div class="who"><span>- NAME SURNAME</span><span class="stars">★★★★★</span></div></article>
  <article class="t-card" style="left:799px;height:322px"><p>Lorem Ipsum is simply dummy text of the printing and typesetting industry. Lorem Ipsum has been the industry's standard dummy text ever since the 1500s, when an unknown printer took a galley of type and scrambled it to make a type specimen book. It has survived not only five centuries, but also the leap into electronic typesetting.</p><div class="who"><span>- NAME SURNAME</span><span class="stars">★★★★★</span></div></article>
</section>

<section class="newsletter">
  <h2>SUBSCRIBE TO OUR NEWSLETTER</h2>
  <p class="text-sm">Lorem Ipsum is simply dummy text of the printing and typesetting industry. Lorem Ipsum has<br>been the industry's standard dummy text ever since the 1500s, when an unknown.</p>
  <form class="subscribe"><span>Enter Your Email</span><a class="btn-blue">SUBSCRIBE</a></form>
</section>

<footer class="site-footer">
  <div class="footer-brand"><div class="sq"></div><span>Marlowe Restoration &amp; Remodeling Group LLC</span></div>
  <h4 style="left:442px">SITEMAP</h4>
  <ul style="left:442px;top:112px"><li>Home</li><li>About us</li><li>Services</li></ul>
  <ul style="left:588px;top:112px"><li>Testimonials</li><li>Contact us</li></ul>
  <h4 style="left:801px">CONTACT INFO</h4>
  <div class="contact-line" style="top:110px"><svg width="16" height="22" viewBox="0 0 16 22"><path d="M8 0a8 8 0 018 8c0 6-8 14-8 14S0 14 0 8a8 8 0 018-8z" fill="#fff"/><circle cx="8" cy="8" r="3" fill="#1a5d9f"/></svg><span>Lorem Ipsum is simply dummy text<br>of the printing and typesetting.</span></div>
  <div class="contact-line" style="top:172px"><svg width="18" height="18" viewBox="0 0 24 24"><path d="M6.6 10.8a15 15 0 006.6 6.6l2.2-2.2a1 1 0 011-.25 11.4 11.4 0 003.6.6 1 1 0 011 1V20a1 1 0 01-1 1A17 17 0 013 4a1 1 0 011-1h3.5a1 1 0 011 1c0 1.25.2 2.45.6 3.6a1 1 0 01-.25 1z" fill="#fff"/></svg><span>555 014 7290</span></div>
</footer>
<div class="copyright">©MARLOWE RESTORATION REMODELING GROUP LLC- 2019. All Rights Reserved.</div>

</body>
</html>
```